Innovative Consulting Firm Needs New Business Cards and Stationary

Our Innovative Consulting Firm, Larkfield Consulting, is in need of new business cards and stationary designs. We want two-sided cards that incorporate our logo, which is attached. We are looking for something not too formal, but is professional and slick.

Card should have the following information:
Name (ex. Owen Hartley)
Title (ex. Manager)
Address (ex. 24680 Cedar Lane)
Address 2 (ex. Suite 100)
City
State
Zip Code
Mobile
Email

The card should also have our website: www.larkfieldconsulting.example

Industry/Entity Type

Management Consulting

Contact Information for Business Card

Name (ex. Owen Hartley)
Title (ex. Manager)
Address 2 (ex. Suite 100)
City
State
Zip Code
Mobile
Email

Font styles to use
Sans Serif

Requirements
Must have
• The colors on the card must match the colors in the logo. The exact color codes are attached in a pdf.
Nice to have
• The Company's Tagline is "Clear Steps, Lasting Gains". This might be nice to incorporate, but not necessary.

```html
<!DOCTYPE html>
<html lang="en">
<head>
<meta charset="utf-8">
<title>Larkfield Consulting – Business Card</title>
<link rel="stylesheet" href="https://fonts.googleapis.com/css2?family=Source+Sans+3:ital,wght@0,400;0,600;1,400&display=swap">
<style>
  :root {
    --navy: #1d4f7c;
    --gold: #f5b21e;
    --ink: #5b5b5b;
    --paper: #ffffff;
    --backdrop: #4a4a4a;
  }
  * { margin: 0; padding: 0; box-sizing: border-box; }
  html, body { width: 1200px; height: 1200px; overflow: hidden; }
  body {
    background: var(--backdrop);
    font-family: "Source Sans 3", sans-serif;
    position: relative;
  }
  .card {
    position: absolute;
    left: 275px;
    width: 649px;
    height: 368px;
    overflow: hidden;
  }
  .card--front { top: 205px; background: var(--paper); }
  .card--back { top: 627px; background: var(--navy); }

  .wordmark {
    position: absolute;
    display: inline-block;
    font-weight: 600;
    line-height: 1;
  }
  .wordmark__name { display: block; font-size: 66px; letter-spacing: 1px; }
  .wordmark__sub { display: block; text-align: right; font-size: 14px; letter-spacing: 7px; margin-top: 2px; margin-right: -7px; }
  .card--front .wordmark { right: 36px; top: 28px; color: var(--navy); }
  .card--back .wordmark { left: 50%; transform: translateX(-50%); top: 98px; color: var(--paper); }
  .card--back .wordmark__name { font-size: 84px; }
  .card--back .wordmark__sub { font-size: 17px; letter-spacing: 8px; margin-right: -8px; margin-top: 2px; }

  .name-tab { position: absolute; left: 0; top: 188px; width: 13px; height: 43px; background: var(--navy); }
  .person { position: absolute; left: 37px; top: 186px; }
  .person__name { font-size: 25px; color: var(--navy); line-height: 1.1; }
  .person__title { font-size: 17px; color: var(--ink); line-height: 1.3; }

  .contact, .address {
    position: absolute;
    top: 249px;
    list-style: none;
    font-size: 16px;
    color: var(--ink);
    line-height: 21.5px;
  }
  .contact { left: 44px; }
  .contact li { display: flex; align-items: center; gap: 9px; white-space: nowrap; }
  .contact svg { width: 14px; height: 14px; flex: none; }
  .address { left: 388px; display: flex; gap: 10px; white-space: nowrap; }
  .address svg { width: 14px; height: 20px; margin-top: 2px; flex: none; }

  .footer-band { position: absolute; left: 0; bottom: 0; width: 649px; height: 23px; }
  .tagline {
    position: absolute;
    left: 440px;
    bottom: 2px;
    font-style: italic;
    font-size: 17px;
    line-height: 20px;
    color: var(--gold);
    white-space: nowrap;
  }
  .back-url {
    position: absolute;
    left: 0; right: 0;
    top: 337px;
    text-align: center;
    color: var(--paper);
    font-size: 17px;
  }
</style>
</head>
<body>
  <section class="card card--front" aria-label="Business card front">
    <div class="wordmark">
      <span class="wordmark__name">Larkfield</span>
      <span class="wordmark__sub">CONSULTING</span>
    </div>

    <div class="name-tab"></div>
    <div class="person">
      <div class="person__name">Owen Hartley</div>
      <div class="person__title">Manager</div>
    </div>

    <ul class="contact">
      <li>
        <svg viewBox="0 0 14 14" aria-hidden="true"><rect x="3" y="0.8" width="8" height="12.4" rx="1.4" fill="none" stroke="var(--navy)" stroke-width="1.6"/><rect x="5.5" y="10.4" width="3" height="1" fill="var(--navy)"/></svg>
        00.000.0000
      </li>
      <li>
        <svg viewBox="0 0 14 14" aria-hidden="true"><rect x="0.5" y="3" width="13" height="9" fill="var(--navy)"/><path d="M0.8 3.4 L7 8 L13.2 3.4" fill="none" stroke="#fff" stroke-width="1.1"/></svg>
        ohartley@larkfieldconsulting.example
      </li>
      <li>
        <svg viewBox="0 0 14 14" aria-hidden="true" fill="none" stroke="var(--navy)" stroke-width="1.1"><circle cx="7" cy="7" r="6"/><ellipse cx="7" cy="7" rx="2.6" ry="6"/><path d="M1 7h12M2 4h10M2 10h10"/></svg>
        www.larkfieldconsulting.example
      </li>
    </ul>

    <div class="address">
      <svg viewBox="0 0 14 20" aria-hidden="true"><path d="M7 0.5a6.2 6.2 0 0 0-6.2 6.2C0.8 11.5 7 19.5 7 19.5s6.2-8 6.2-12.8A6.2 6.2 0 0 0 7 0.5z" fill="var(--navy)"/><circle cx="7" cy="6.7" r="2.3" fill="#fff"/></svg>
      <div>24680 Cedar Lane<br>Suite 100<br>City, State Zip Code</div>
    </div>

    <svg class="footer-band" viewBox="0 0 649 23" aria-hidden="true">
      <polygon points="0,10 413,10 408,23 0,23" fill="var(--gold)"/>
      <polygon points="413,10 418,10 410,23 406,23" fill="var(--paper)"/>
      <polygon points="425,0 649,0 649,23 415,23" fill="var(--navy)"/>
    </svg>
    <div class="tagline">Clear Steps, Lasting Gains</div>
  </section>

  <section class="card card--back" aria-label="Business card back">
    <div class="wordmark">
      <span class="wordmark__name">Larkfield</span>
      <span class="wordmark__sub">CONSULTING</span>
    </div>
    <div class="back-url">www.larkfieldconsulting.example</div>
  </section>
</body>
</html>
```